BRH

Please see our existing website at www.brightriverhealth.com.au
We want to keep the same content and photos but need a new design as the current one looks too clinical and boring.

```html
<!DOCTYPE html>
<html lang="en">
<head>
<meta charset="utf-8">
<title>Bright River Health – Website Design</title>
<link rel="stylesheet" href="https://fonts.googleapis.com/css2?family=Montserrat:wght@300;400;500;600;700;800&display=swap">
<style>
:root{
  --green:#5fb940;
  --green-dark:#46a02c;
  --green-soft:#e6f3dc;
  --band:#e3f1d8;
  --ink:#1f1f1f;
  --text:#6b6b6b;
  --grey:#f2f2f2;
  --line:#dcdcdc;
  --white:#fff;
  --photo-a:#5b5f64;
  --photo-b:#2f3236;
}
*{box-sizing:border-box;margin:0;padding:0}
html,body{width:1200px;height:3750px;overflow:hidden}
body{background:#f6f9f2;font-family:"Montserrat",sans-serif;color:var(--ink);position:relative}
.backdrop{position:absolute;inset:0}
.brand-mark{position:absolute;top:44px;left:0;width:1200px;text-align:center;font-weight:800;font-size:30px;letter-spacing:2px;color:var(--green-dark);line-height:1.05}
.side-label{position:absolute;font-weight:300;font-size:19px;letter-spacing:12px;color:var(--green);white-space:nowrap;transform:rotate(-90deg);transform-origin:center}
.side-label.mobile{left:-40px;top:2170px;width:280px;text-align:center}
.side-label.desktop{left:960px;top:1935px;width:290px;text-align:center}

.page{position:absolute;background:var(--white);overflow:hidden;box-shadow:0 4px 18px rgba(0,0,0,.08)}
.page.desktop{left:378px;top:750px;width:688px;height:2395px}
.page.mobile{left:143px;top:750px;width:173px;height:2905px}

.topbar{background:var(--green);color:#fff;display:flex;align-items:center;justify-content:center;gap:10px;font-size:5px;position:relative}
.topbar .quote{position:absolute;right:0;top:0;bottom:0;background:var(--green-dark);color:#fff;font-weight:700;display:flex;align-items:center;padding:0 16px;font-size:5.5px}
.header{display:flex;align-items:center;justify-content:space-between;background:#fff;border-bottom:1px solid #eee}
.logo{font-weight:800;color:var(--green-dark);letter-spacing:.5px;line-height:1}
.nav{display:flex;gap:14px;font-size:5.5px;font-weight:600;color:var(--ink)}
.nav .active{color:var(--green);border-bottom:1px solid var(--green)}
.burger{width:12px;height:8px;border-top:1.5px solid #555;border-bottom:1.5px solid #555;position:relative}
.burger::after{content:"";position:absolute;left:0;right:0;top:2px;border-top:1.5px solid #555}
.photo{background:linear-gradient(135deg,var(--photo-a),var(--photo-b))}
.hero{position:relative;display:flex;flex-direction:column;align-items:center;justify-content:center;text-align:center;color:#fff}
.hero .photo{position:absolute;inset:0}
.hero .shade{position:absolute;inset:0;background:rgba(20,20,20,.25)}
.hero > *:not(.photo):not(.shade){position:relative}
.tagline{color:var(--green);letter-spacing:3px;font-weight:500}
.hero h1{font-weight:800;text-transform:uppercase;line-height:1.15}
.hero h1 .outline{color:transparent;-webkit-text-stroke:1px #fff}
.btn{display:inline-block;background:var(--green);color:#fff;font-weight:700;text-transform:uppercase}
.btn.ghost{background:transparent;border:1px solid #fff}
.eyebrow{color:var(--green);font-size:5px;letter-spacing:1.5px;text-transform:uppercase;font-weight:500}
.body{color:var(--text);line-height:1.75}
.body a{color:var(--green);text-decoration:underline}
.ticks{list-style:none;display:grid;color:var(--green);font-weight:500}
.ticks li{display:flex;align-items:center;gap:4px}
.ticks li::before{content:"";width:5px;height:5px;border:1px solid var(--green);border-radius:50%;flex:none}
.video{position:relative;border:1px solid var(--green)}
.video .play{position:absolute;left:50%;top:50%;transform:translate(-50%,-50%)}
.dots{display:flex;gap:5px;justify-content:center}
.dots span{width:5px;height:5px;border-radius:50%;background:#bfe0ae}
.dots span.on{background:var(--green);box-shadow:0 0 0 2px #d7eccb}
.field{border:1px solid var(--line);background:#fff;color:#888;display:flex;align-items:center;justify-content:space-between}
.check{display:flex;align-items:center;gap:4px;color:#444}
.check::before{content:"";width:5px;height:5px;border:1px solid #bbb;flex:none}
.footer{background:var(--grey)}
.footer h4{color:var(--green);font-weight:600}
.social{display:inline-block;width:8px;height:8px;border-radius:2px;background:var(--green-soft);border:1px solid var(--green);vertical-align:middle;margin-left:3px}
.copy{background:var(--green);color:#fff;text-align:center;display:flex;align-items:center;justify-content:center}

/* desktop */
.desktop .topbar{height:20px}
.desktop .header{height:50px;padding:0 92px}
.desktop .logo{font-size:14px}
.desktop .hero{height:383px}
.desktop .tagline{font-size:9px;margin-bottom:8px}
.desktop .hero h1{font-size:26px}
.desktop .hero .btn{font-size:6px;padding:8px 16px;margin-top:24px}
.desktop .intro{height:159px;background:var(--grey);display:grid;grid-template-columns:200px 1fr;gap:25px;padding:40px 92px 0}
.desktop .intro h2{font-size:12px;font-weight:600;line-height:1.45;margin-top:4px}
.desktop .body{font-size:5.5px}
.desktop .about{height:327px;display:grid;grid-template-columns:187px 1fr;gap:28px;padding:37px 92px 0}
.desktop .about .video{height:247px}
.desktop .about h2{font-size:12px;font-weight:600;line-height:1.35;margin:4px 0 10px}
.desktop .ticks{grid-template-columns:1fr 1fr;gap:7px 8px;font-size:5.3px;margin:12px 0}
.desktop .about .btn{font-size:5.5px;padding:8px 14px;margin-top:14px}
.desktop .equipment{height:527px;background:var(--grey);text-align:center;padding:40px 92px 0}
.desktop .equipment h2{font-size:13px;font-weight:600;margin:4px 0 14px}
.desktop .equipment .body{margin-bottom:7px}
.desktop .equipment .photo{height:272px;margin:4px 0 16px}
.desktop .equipment .note{font-size:5.5px;font-weight:600;margin-top:12px}
.desktop .trainers{height:296px;display:grid;grid-template-columns:385px 1fr;background:var(--green)}
.desktop .trainers .copybox{color:#fff;padding:44px 40px 0 92px;position:relative}
.desktop .trainers h2{font-size:13px;font-weight:600;line-height:1.3;margin-bottom:14px}
.desktop .trainers .body{color:#eaf6e2;margin-bottom:8px}
.desktop .trainers .btn{font-size:5.5px;padding:7px 12px;margin-top:12px}
.desktop .booking{height:430px;padding:40px 178px 0;text-align:center}
.desktop .booking h2{font-size:12.5px;font-weight:600;line-height:1.4;margin-bottom:22px}
.desktop .row{display:grid;grid-template-columns:1fr 1fr;gap:8px;margin-bottom:8px}
.desktop .field{height:20px;font-size:5.3px;padding:0 8px}
.desktop .hint{font-size:5px;color:#999;text-align:left;margin:6px 0}
.desktop .checks{display:grid;grid-template-columns:repeat(3,auto);gap:7px 10px;font-size:5px;text-align:left;justify-content:start;margin-bottom:8px}
.desktop .checks .wide{grid-column:1 / -1}
.desktop .field.area{height:42px;align-items:flex-start;padding-top:6px}
.desktop .booking .btn{font-size:5.5px;padding:8px 14px;margin-top:20px}
.desktop .footer{height:182px;display:grid;grid-template-columns:1fr 180px 140px;padding:40px 92px 0}
.desktop .footer .logo{font-size:13px;margin-bottom:18px}
.desktop .footer h4{font-size:9px;margin-bottom:18px}
.desktop .footer ul{list-style:none;font-size:5.3px;color:#555;line-height:2.6}
.desktop .contact{font-size:5.3px;color:#555;line-height:1.6}
.desktop .contact div{display:flex;gap:6px;margin-bottom:7px;align-items:flex-start}
.desktop .copy{height:22px;font-size:5.3px}

/* mobile */
.mobile .topbar{height:17px;gap:6px;font-size:4px}
.mobile .header{height:41px;padding:0 10px}
.mobile .logo{font-size:9px}
.mobile .hero{height:231px;padding:0 8px}
.mobile .tagline{font-size:5px;letter-spacing:1.5px;margin-bottom:6px}
.mobile .hero h1{font-size:14px;line-height:1.3}
.mobile .hero .btn{font-size:4.5px;padding:7px 12px;margin-top:12px}
.mobile .sec{padding:0 10px}
.mobile .body{font-size:4.6px}
.mobile h2{font-size:8.5px;font-weight:600;line-height:1.4;margin:3px 0 10px}
.mobile .eyebrow{font-size:4.2px}
.mobile .intro{height:242px;padding-top:32px}
.mobile .about{height:575px;background:var(--grey);padding-top:36px}
.mobile .about .video{height:190px;margin-bottom:28px}
.mobile .ticks{grid-template-columns:1fr;gap:5px;font-size:4.3px;margin:10px 0}
.mobile .btn{font-size:4.5px;padding:7px 12px;margin-top:12px}
.mobile .equipment{height:422px;padding-top:32px}
.mobile .equipment .photo{height:95px;margin:12px 0 10px}
.mobile .equipment .note{font-size:4.5px;font-weight:600;text-align:center;margin-top:14px;line-height:1.6}
.mobile .trainers{height:296px;background:var(--green);color:#fff;padding-top:36px}
.mobile .trainers .body{color:#eaf6e2;margin-bottom:6px}
.mobile .trainer-photo{height:148px}
.mobile .booking{height:546px;padding-top:36px}
.mobile .field{height:17px;font-size:4.3px;padding:0 6px;margin-bottom:8px}
.mobile .hint{font-size:4.2px;color:#999;margin:4px 0 8px}
.mobile .checks{display:grid;gap:6px;font-size:4.2px;margin-bottom:8px}
.mobile .field.area{height:36px;align-items:flex-start;padding-top:5px}
.mobile .footer{height:364px;padding-top:32px}
.mobile .footer .logo{font-size:9px;margin-bottom:10px}
.mobile .footer h4{font-size:7.5px;margin:22px 0 12px}
.mobile .footer ul{list-style:none;font-size:4.3px;color:#555;line-height:2.5}
.mobile .contact{font-size:4.3px;color:#555;line-height:1.6}
.mobile .contact div{display:flex;gap:5px;margin-bottom:6px}
.mobile .copy{height:22px;font-size:4.3px}
</style>
</head>
<body>

<svg class="backdrop" width="1200" height="3750" viewBox="0 0 1200 3750" aria-hidden="true">
  <polygon points="700,0 1200,0 1200,180 420,3750 380,3750" fill="var(--band)"/>
  <polygon points="1200,900 1200,1300 560,3750 470,3750" fill="#edf6e5"/>
</svg>

<div class="brand-mark">BRIGHT RIVER<br>HEALTH</div>

<div class="side-label mobile">RESPONSIVE SIDE</div>
<div class="side-label desktop">LAPTOP / DESKTOP</div>

<main class="page desktop">
  <div class="topbar"><span>✉ hello@brightriver.com</span><span>☏ 07 5500 0142</span><span class="quote">FREE QUOTE</span></div>
  <header class="header">
    <div class="logo">BRIGHT RIVER<br>HEALTH</div>
    <nav class="nav"><span class="active">HOME</span><span>ABOUT US ⌄</span><span>OUR SERVICES ⌄</span><span>RESOURCES ⌄</span><span>TESTIMONIALS</span><span>CONTACT</span></nav>
  </header>
  <section class="hero">
    <div class="photo" role="img" aria-label="Trainer guiding a client on a strength machine in the gym"></div>
    <div class="shade"></div>
    <p class="tagline">FEEL FITTER. MOVE BETTER. HEALTHIER!</p>
    <h1>Reduce <span class="outline">Pain.</span> Improve <span class="outline">Strength.</span><br>Increase <span class="outline">Mobility</span> &amp; <span class="outline">Movement.</span></h1>
    <a class="btn">Get Started</a>
  </section>
  <section class="intro">
    <div><p class="eyebrow">Introduction</p><h2>Specialised in injury free functional training with specialised FlexCore Machines</h2></div>
    <p class="body">Let's paint the picture. You want to overcome existing pain or back injury, but the traditional exercises make it worse. Or perhaps you want to feel fitter and move more flexible, but high intensity, sweaty gym classes with the risk of injury just aren't your thing. At the Bright River Health centre our specialist trainers, small group sessions, and top-of-the-range <a>FlexCore machines</a> mean you can build strength and mobility while preventing future pain and injury.</p>
  </section>
  <section class="about">
    <div class="video photo" role="img" aria-label="Video still of a trainer assisting a client with a floor exercise">
      <svg class="play" width="28" height="28" viewBox="0 0 28 28"><circle cx="14" cy="14" r="14" fill="#5fb940"/><path d="M11 8l9 6-9 6z" fill="#fff"/></svg>
    </div>
    <div>
      <p class="eyebrow">About us</p>
      <h2>Is The Bright River Health Centre<br>A Good Fit For You?</h2>
      <p class="body">If you relate to any of the following, then the answer to this question is a resounding 'yes!'</p>
      <ul class="ticks">
        <li>Feel old and tired</li><li>Have a recurring sore back or neck</li>
        <li>Have an existing injury</li><li>Want more strength and endurance</li>
        <li>Not interested in a traditional gym</li><li>Feel limited in mobility and flexibility</li>
        <li>Too stiff to move the way you want</li><li>Prefer small group or one-on-one training</li>
      </ul>
      <p class="body">There's no need to endure these issues. At the Bright River Health centre we couple state-of-the-art <a>FlexCore machines</a> with knowledgeable trainers and functional fitness programs so that you can isolate, address and overcome these issues.</p>
      <a class="btn">Learn More</a>
    </div>
  </section>
  <section class="equipment">
    <p class="eyebrow">FlexCore Equipment</p>
    <h2>What Is FlexCore Equipment?</h2>
    <p class="body">FlexCore are the world leaders in specialised medical strengthening machines. They can measure and build isolated groups of muscles, as well as the endurance and flexibility. All FlexCore products are based on scientifically proven technologies, which is perhaps why professional athletes like Sam Carter trust machines like the Rotary Torso to increase range of movement, rehabilitate, and prevent injury.</p>
    <p class="body">Our range of world class <a>FlexCore machines</a> address this. At Bright River Health, we use this equipment to create personal programs that work around any injuries and limitations you may have, to build functional strength and mobility in your body.</p>
    <div class="photo" role="img" aria-label="Trainer assisting a client using an overhead strength machine"></div>
    <div class="dots"><span></span><span class="on"></span><span></span></div>
    <p class="note">Think this might be what you're looking for? <span class="body">Try a <a>complimentary session</a> today to find out!</span></p>
  </section>
  <section class="trainers">
    <div class="copybox">
      <h2>Qualified And Experienced<br>Personal Trainers in<br>Riverton / Eastbrook Coast</h2>
      <p class="body">Our personal trainers are highly qualified experts in functional training for people of all ages and abilities. We can ensure you'll get the best personal trainer for your specific needs and goals.</p>
      <p class="body">Our trainers will not simply push you to go 'as hard and fast as you can'. You will receive a carefully put together workout plan that targets your specific requirements to carefully and efficiently build up your functional strength and mobility.</p>
      <a class="btn ghost">Our Trainers</a>
    </div>
    <div class="photo" role="img" aria-label="Trainers working out in a gym with bright green lit walls"></div>
  </section>
  <section class="booking">
    <h2>Book your complimentary personal<br>training session now!</h2>
    <div class="row"><div class="field">Your Name*</div><div class="field">Your Email Address*</div></div>
    <div class="row"><div class="field">Your Phone Number*</div><div class="field">Your Age*</div></div>
    <p class="hint">Tell us more about you so that we may be able to assist you better. Please tick all that apply:</p>
    <div class="checks">
      <span class="check wide">Back, Spinal and/or Neck Pain, Injury, Conditioning</span>
      <span class="check">Injury and Rehabilitation</span><span class="check">Functional Fitness</span><span class="check">Personal Training</span>
      <span class="check">Core Strength/Condition</span><span class="check">Mobility/Flexibility</span><span class="check">Injury Prevention</span>
      <span class="check">Sports Specific Training</span><span class="check">Weight Loss</span><span class="check">Health &amp; Wellbeing</span>
    </div>
    <p class="hint">Please select when you would like to be contacted:</p>
    <div class="row"><div class="field">Phone* <span>⌄</span></div><div class="field">Anytime* <span>⌄</span></div></div>
    <div class="field area">Anything else you would like to let us know?</div>
    <a class="btn">Submit Form</a>
  </section>
  <footer class="footer">
    <div><div class="logo">BRIGHT RIVER<br>HEALTH</div><p class="body" style="width:150px">Lorem ipsum dolor sit amet, tempor incididunt ut labore et dolore magna aliqua, commodo viverra maecenas accumsan lacus vel facilisis.</p></div>
    <div><h4>Quick Links</h4><ul><li>Home</li><li>About Us</li><li>Services</li><li>Resources</li></ul></div>
    <div class="contact"><h4>Get in Touch</h4>
      <div><svg width="6" height="8" viewBox="0 0 6 8"><path d="M3 0a3 3 0 0 1 3 3c0 2-3 5-3 5S0 5 0 3a3 3 0 0 1 3-3z" fill="#5fb940"/><circle cx="3" cy="3" r="1" fill="#fff"/></svg><span>4/22 Lakeside Parade<br>Riverton QLD 4200</span></div>
      <div><svg width="7" height="7" viewBox="0 0 7 7"><path d="M1 0l2 1-1 1.5a4 4 0 0 0 2.5 2.5L6 4l1 2-1 1C3 7 0 4 0 1z" fill="#5fb940"/></svg><span>07 5500 0142</span></div>
      <div>Find Us At <span class="social"></span><span class="social"></span></div>
    </div>
  </footer>
  <div class="copy">Copyright © 2021 Bright River Health.</div>
</main>

<main class="page mobile">
  <div class="topbar"><span>✉ hello@brightriver.com</span><span>☏ 07 5500 0142</span></div>
  <header class="header"><div class="logo">BRIGHT RIVER<br>HEALTH</div><div class="burger"></div></header>
  <section class="hero">
    <div class="photo" role="img" aria-label="Trainer guiding a client on a strength machine"></div>
    <div class="shade"></div>
    <p class="tagline">FEEL FITTER. MOVE BETTER. HEALTHIER!</p>
    <h1>Reduce <span class="outline">Pain.</span><br>Improve <span class="outline">Strength.</span><br>Increase <span class="outline">Mobility</span><br>&amp; <span class="outline">Movement.</span></h1>
    <a class="btn">Get Started</a>
  </section>
  <section class="sec intro">
    <p class="eyebrow">Introduction</p>
    <h2>Specialised in injury free functional training with specialised FlexCore Machines</h2>
    <p class="body">Let's paint the picture. You want to overcome existing pain or back injury, but the traditional exercises make it worse. Or perhaps you want to feel fitter and more flexible, but high intensity, sweaty gym classes with the risk of injury just aren't your thing. At the Bright River Health centre our specialist trainers, small group sessions, and top-of-the-range <a>FlexCore machines</a> mean you can build strength and mobility while preventing future pain and injury.</p>
  </section>
  <section class="sec about">
    <div class="video photo" role="img" aria-label="Video still of a trainer assisting a client with a floor exercise">
      <svg class="play" width="22" height="22" viewBox="0 0 28 28"><circle cx="14" cy="14" r="14" fill="#5fb940"/><path d="M11 8l9 6-9 6z" fill="#fff"/></svg>
    </div>
    <p class="eyebrow">About us</p>
    <h2>Is The Bright River Health Centre A Good Fit For You?</h2>
    <p class="body">If you relate to any of the following, then the answer to this question is a resounding 'yes!'</p>
    <ul class="ticks">
      <li>Feel old and tired</li><li>Have an existing injury</li><li>Not interested in a traditional gym</li><li>Too stiff to move the way you want</li><li>Have a recurring sore back or neck</li><li>Want more strength and endurance</li><li>Feel limited in mobility and flexibility</li><li>Prefer small group or one-on-one training</li>
    </ul>
    <p class="body">There's no need to endure these issues. At the Bright River Health centre we couple state-of-the-art <a>FlexCore machines</a> with knowledgeable trainers and functional fitness programs so that you can isolate, address and overcome these issues.</p>
    <a class="btn">Learn More</a>
  </section>
  <section class="sec equipment">
    <p class="eyebrow">FlexCore Equipment</p>
    <h2>What Is FlexCore Equipment?</h2>
    <p class="body">FlexCore are the world leaders in specialised medical strengthening machines. They can measure and build isolated groups of muscles, as well as the endurance and flexibility. All FlexCore products are based on scientifically proven technologies, which is perhaps why professional athletes like Sam Carter trust machines like the Rotary Torso to increase range of movement, rehabilitate, and prevent injury.</p>
    <p class="body" style="margin-top:6px">Our range of world class <a>FlexCore machines</a> address this. At Bright River Health, we use this equipment to create personal programs that work around any injuries and limitations you may have, to build functional strength and mobility in your body.</p>
    <div class="photo" role="img" aria-label="Trainer assisting a client using an overhead strength machine"></div>
    <div class="dots"><span></span><span class="on"></span><span></span></div>
    <p class="note">Think this might be what you're looking for?<br><span class="body">Try a <a>complimentary session</a> today to find out!</span></p>
  </section>
  <section class="sec trainers">
    <h2>Qualified And Experienced Personal Trainers in Riverton / Eastbrook Coast</h2>
    <p class="body">Our personal trainers are highly qualified experts in functional training for people of all ages and abilities. We can ensure you'll get the best personal trainer for your specific needs and goals.</p>
    <p class="body">Our trainers will not simply push you to go 'as hard and fast as you can'. You will receive a carefully put together workout plan that targets your specific requirements to carefully and efficiently build up your functional strength and mobility without injury.</p>
    <a class="btn ghost">Our Trainers</a>
  </section>
  <div class="photo trainer-photo" role="img" aria-label="Trainers working out in a gym with bright green lit walls"></div>
  <section class="sec booking">
    <h2>Book your complimentary personal training session now!</h2>
    <div class="field">Your Name*</div><div class="field">Your Email Address*</div><div class="field">Your Phone Number*</div><div class="field">Your Age*</div>
    <p class="hint">Tell us more about you so that we may be able to assist you better. Please tick all that apply:</p>
    <div class="checks">
      <span class="check">Back, Spinal and/or Neck Pain, Injury, Conditioning</span><span class="check">Injury and Rehabilitation</span><span class="check">Functional Fitness</span><span class="check">Personal Training</span><span class="check">Core Strength/Condition</span><span class="check">Mobility/Flexibility</span><span class="check">Injury Prevention</span><span class="check">Sports Specific Training</span><span class="check">Weight Loss</span><span class="check">Health &amp; Wellbeing</span>
    </div>
    <p class="hint">Please select when you would like to be contacted:</p>
    <div class="field">Phone* <span>⌄</span></div><div class="field">Anytime* <span>⌄</span></div>
    <div class="field area">Anything else you would like to let us know?</div>
    <a class="btn">Submit Form</a>
  </section>
  <footer class="sec footer">
    <div class="logo">BRIGHT RIVER<br>HEALTH</div>
    <p class="body">Lorem ipsum dolor sit amet, tempor incididunt ut labore et dolore magna aliqua, commodo viverra maecenas accumsan lacus vel facilisis.</p>
    <h4>Quick Links</h4><ul><li>Home</li><li>About Us</li><li>Services</li><li>Resources</li></ul>
    <div class="contact"><h4>Get in Touch</h4>
      <div><svg width="6" height="8" viewBox="0 0 6 8"><path d="M3 0a3 3 0 0 1 3 3c0 2-3 5-3 5S0 5 0 3a3 3 0 0 1 3-3z" fill="#5fb940"/><circle cx="3" cy="3" r="1" fill="#fff"/></svg><span>4/22 Lakeside Parade<br>Riverton QLD 4200</span></div>
      <div><svg width="7" height="7" viewBox="0 0 7 7"><path d="M1 0l2 1-1 1.5a4 4 0 0 0 2.5 2.5L6 4l1 2-1 1C3 7 0 4 0 1z" fill="#5fb940"/></svg><span>07 5500 0142</span></div>
      <div>Find Us At <span class="social"></span><span class="social"></span></div>
    </div>
  </footer>
  <div class="copy">Copyright © 2021 Bright River Health.</div>
</main>

</body>
</html>
```